letter head for a construction company

Company Name: Zaviro Construction Limited

Address: Kilele Street, Tengeru Shores, Dar es salaam, Tanzania

Phone: 0754382916

email : info@zaviroconstruction.example

website : www.zaviroconstruction.example

```html
<!DOCTYPE html>
<html lang="en">
<head>
<meta charset="utf-8">
<title>Zaviro Construction Limited — Letterhead</title>
<link href="https://fonts.googleapis.com/css2?family=Montserrat:wght@400;500;600;700&family=Raleway:wght@400;500&display=swap" rel="stylesheet">
<style>
  :root {
    --backdrop: #ececee;
    --paper: #ffffff;
    --ink: #1f1f24;
    --ink-soft: #6b6b72;
    --body-text: #8a8a90;
    --accent: #e8781e;
    --rule: #2a2a30;
    --dots: #e6e6ea;
  }
  * { box-sizing: border-box; margin: 0; padding: 0; }
  html, body {
    width: 1200px; height: 800px; overflow: hidden;
    background: var(--backdrop);
  }
  .canvas {
    width: 1200px; height: 800px;
    display: flex; align-items: center; justify-content: center;
  }
  .letterhead {
    position: relative;
    width: 556px; height: 786px;
    background: var(--paper);
    box-shadow: 0 2px 10px rgba(0,0,0,0.08);
    overflow: hidden;
    font-family: "Raleway", sans-serif;
  }
  .backdrop-texture {
    position: absolute; left: 0; right: 0; top: 400px; bottom: 0;
    background: radial-gradient(ellipse at 40% 80%, var(--dots) 0%, rgba(236,236,240,0.5) 45%, rgba(255,255,255,0) 75%);
  }
  .brand {
    position: absolute; top: 50px; left: 0; right: 0;
    display: flex; align-items: center; justify-content: center; gap: 8px;
  }
  .brand-mark {
    width: 12px; height: 12px; background: var(--accent);
  }
  .brand-name {
    font-family: "Montserrat", sans-serif;
    font-weight: 700; font-size: 15px; letter-spacing: 0.5px;
    color: var(--ink);
  }
  .header-rule {
    position: absolute; top: 96px; left: 16px; right: 16px;
    height: 1px; background: var(--rule);
  }
  .header-accent {
    position: absolute; top: 94px; left: 198px; width: 160px;
    height: 4px; background: var(--accent);
  }
  .letter {
    position: absolute; top: 170px; left: 70px; right: 62px;
  }
  .recipient-name {
    font-family: "Montserrat", sans-serif;
    font-weight: 700; font-size: 11px; color: var(--ink);
  }
  .recipient-role {
    font-size: 8px; color: var(--ink-soft); margin-bottom: 16px;
  }
  .letter p {
    font-size: 8.3px; line-height: 12px; color: var(--body-text);
    text-align: justify; margin-bottom: 16px;
  }
  .sign-off {
    position: absolute; top: 572px; right: 62px; text-align: right;
  }
  .signature {
    width: 150px; height: 22px; margin-left: auto; margin-bottom: 4px;
    background: linear-gradient(90deg, rgba(232,120,30,0) 0%, rgba(232,120,30,0.35) 30%, rgba(232,120,30,0.35) 70%, rgba(232,120,30,0) 100%);
    border-radius: 11px;
  }
  .signer-name {
    font-family: "Montserrat", sans-serif;
    font-weight: 700; font-size: 11px; color: var(--ink);
  }
  .signer-role { font-size: 8px; color: var(--ink-soft); }
  .contacts {
    position: absolute; top: 668px; left: 100px; right: 50px;
    display: flex; justify-content: space-between; align-items: flex-end;
  }
  .contact {
    display: flex; flex-direction: column; align-items: center; gap: 5px;
    font-family: "Montserrat", sans-serif;
    font-size: 9px; color: var(--ink); text-align: center; line-height: 11px;
  }
  .contact.phone { font-weight: 700; letter-spacing: 1px; }
  .contact-icon { width: 13px; height: 13px; }
  .footer-band {
    position: absolute; left: 70px; right: 16px; bottom: 22px;
    height: 20px; background: var(--accent);
    border-radius: 8px 8px 0 0;
  }
</style>
</head>
<body>
<main class="canvas">
  <article class="letterhead">
    <div class="backdrop-texture" role="img" aria-label="Soft halftone dot pattern in light grey"></div>

    <header>
      <div class="brand">
        <span class="brand-mark"></span>
        <span class="brand-name">Zaviro Construction Limited</span>
      </div>
      <div class="header-rule"></div>
      <div class="header-accent"></div>
    </header>

    <section class="letter">
      <div class="recipient-name">Dear. Mr Mwakasege</div>
      <div class="recipient-role">General Manager</div>
      <p>Lorem ipsum dolor sit amet, consectetur adipisicing elit, sed do eiusmod tempor incididunt ut labore et dolore magna aliqua. Ut enim ad minim veniam, quis nostrud exercitation ullamco laboris nisi ut aliquip ex ea commodo consequat. Duis aute irure dolor in reprehenderit in voluptate velit esse cillum dolore eu fugiat nulla pariatur. Excepteur sint occaecat cupidatat non proident, sunt in culpa qui officia deserunt mollit anim id est laborum. Sed ut perspiciatis unde omnis iste natus error sit voluptatem accusantium doloremque laudantium, totam rem aperiam, eaque ipsa quae ab illo inventore veritatis et quasi architecto beatae vitae dicta sunt explicabo. Nemo enim ipsam voluptatem quia voluptas sit aspernatur aut odit aut fugit, sed quia consequuntur magni dolores eos qui ratione voluptatem sequi nesciunt. Neque porro voluptatem sequi nesciunt. Nemo enim ipsam voluptatem quia voluptas.</p>
      <p>Lorem ipsum dolor sit amet, consectetur adipisicing elit, sed do eiusmod tempor incididunt ut labore et dolore magna aliqua. Ut enim ad minim veniam, quis nostrud exercitation ullamco laboris nisi ut aliquip ex ea commodo consequat. Duis aute irure dolor in reprehenderit in voluptate velit esse cillum dolore eu fugiat nulla pariatur. Excepteur sint occaecat cupidatat non proident, sunt in culpa qui officia deserunt mollit anim id est laborum. Sed ut perspiciatis unde omnis iste natus error sit voluptatem accusantium doloremque laudantium, totam rem aperiam, eaque ipsa quae ab illo inventore veritatis et quasi architecto beatae vitae dicta sunt explicabo. Nemo enim ipsam voluptatem quia voluptas sit aspernatur aut odit aut.</p>
      <p>Lorem ipsum dolor sit amet, consectetur adipisicing elit, sed do eiusmod tempor incididunt ut labore et dolore magna aliqua. Ut enim ad minim veniam, quis nostrud exercitation ullamco laboris nisi ut aliquip ex ea commodo consequat. Duis aute irure dolor in reprehenderit in voluptate velit esse cillum dolore eu fugiat nulla pariatur. Excepteur sint occaecat cupidatat non proident, sunt in culpa qui officia deserunt mollit anim id est laborum.</p>
    </section>

    <div class="sign-off">
      <div class="signature" role="img" aria-label="Handwritten signature in orange"></div>
      <div class="signer-name">Daniel Mwakasege</div>
      <div class="signer-role">General Manager</div>
    </div>

    <footer class="contacts">
      <div class="contact phone">
        <svg class="contact-icon" viewBox="0 0 14 14" aria-hidden="true">
          <circle cx="7" cy="7" r="6.2" fill="none" stroke="var(--accent)" stroke-width="1.2"/>
          <path d="M4.6 4.2c.3-.3.7-.3.9 0l.7.9c.2.3.1.6-.1.8l-.3.3c.3.7.9 1.3 1.6 1.6l.3-.3c.2-.2.5-.3.8-.1l.9.7c.3.2.3.6 0 .9l-.4.4c-.4.4-1 .5-1.5.2-1.3-.7-2.4-1.8-3.1-3.1-.3-.5-.2-1.1.2-1.5z" fill="var(--accent)"/>
        </svg>
        <span>0754382916</span>
      </div>
      <div class="contact">
        <svg class="contact-icon" viewBox="0 0 14 14" aria-hidden="true">
          <circle cx="7" cy="7" r="6.2" fill="none" stroke="var(--accent)" stroke-width="1.2"/>
          <rect x="4" y="4.8" width="6" height="4.4" rx="0.5" fill="var(--accent)"/>
          <path d="M4.2 5l2.8 2.2L9.8 5" fill="none" stroke="#fff" stroke-width="0.7"/>
        </svg>
        <span>info@zaviroconstruction.example<br>www.zaviroconstruction.example</span>
      </div>
      <div class="contact">
        <svg class="contact-icon" viewBox="0 0 14 14" aria-hidden="true">
          <circle cx="7" cy="7" r="6.2" fill="none" stroke="var(--accent)" stroke-width="1.2"/>
          <path d="M7 3.6c-1.3 0-2.3 1-2.3 2.3 0 1.7 2.3 4.3 2.3 4.3s2.3-2.6 2.3-4.3c0-1.3-1-2.3-2.3-2.3z" fill="var(--accent)"/>
          <circle cx="7" cy="5.9" r="0.8" fill="#fff"/>
        </svg>
        <span>Kilele Street, Tengeru<br>Shores, Dar es salaam,<br>Tanzania</span>
      </div>
    </footer>

    <div class="footer-band"></div>
  </article>
</main>
</body>
</html>
```